Updated Power Point template design

We need an updated Power Point design template. Please see attach business card for branding, would like to incorporate the blue and black corner design aspect some how.

Attached a sample of current PP

Target Market(s)

Corporate Clients

Industry/Entity Type

Electronics

Requirements
Must have
• We require a whole slide deck ( Title side etc )
Nice to have
• Nice amount of white space on slide

```html
<!DOCTYPE html>
<html lang="en">
<head>
<meta charset="utf-8">
<title>Ridgeline Components – Slide Deck Template</title>
<link href="https://fonts.googleapis.com/css2?family=Open+Sans:wght@400;600;700&family=Dosis:wght@400&display=swap" rel="stylesheet">
<style>
  :root{
    --stage:#8d8d8d;
    --blue:#0a6fbf;
    --black:#0b0b0b;
    --white:#ffffff;
    --ink:#1a1a1a;
    --toc:#5a5347;
  }
  *{box-sizing:border-box;margin:0;padding:0}
  html,body{width:1200px;height:1200px;overflow:hidden;background:var(--stage)}
  .deck{position:relative;width:1200px;height:1200px}
  .slide{position:absolute;width:546px;height:409px;background:var(--white);overflow:hidden;
    box-shadow:6px 8px 10px rgba(0,0,0,.55);font-family:"Open Sans",sans-serif}
  .slide--title{left:43px;top:129px;width:541px}
  .slide--contents{left:616px;top:129px}
  .slide--content{left:43px;top:582px}
  .slide--closing{left:616px;top:582px}
  .slide svg.art{position:absolute;inset:0;width:100%;height:100%}

  .brand{position:absolute;font-family:"Open Sans",sans-serif;font-weight:700;color:var(--blue);
    white-space:nowrap;display:flex;align-items:center;gap:6px}
  .brand::before{content:"";width:var(--dot);height:var(--dot);background:var(--blue);border-radius:50%}
  .brand--lg{right:36px;top:64px;font-size:15px;--dot:12px}
  .brand--sm{right:14px;top:30px;font-size:8px;--dot:7px}
  .brand--foot{left:22px;top:356px;font-size:13px;--dot:10px}

  .cover-title{position:absolute;right:35px;top:158px;text-align:right}
  .cover-title h1{font-weight:600;font-size:32px;color:var(--blue);letter-spacing:.2px;line-height:1.1}
  .cover-title p{font-weight:600;font-size:15px;color:var(--ink);line-height:1.2;margin-top:4px}

  .band-title{position:absolute;left:0;top:19px;height:43px;display:flex;align-items:center;
    padding-left:61px;color:var(--white);font-weight:600;font-size:19.5px}
  .slide--content .band-title{padding-left:46px}

  .toc{position:absolute;left:61px;top:84px;width:440px;font-family:"Dosis",sans-serif;color:var(--toc);list-style:none}
  .toc li{display:flex;align-items:flex-end;height:18px;font-size:10px}
  .toc li.sub{padding-left:27px;font-size:7.5px}
  .toc .lead{flex:1;border-bottom:1px dotted var(--toc);margin:0 2px 3px}
  .toc .num{width:50px;text-align:right;padding-right:12px;font-size:9px}

  .body-head{position:absolute;left:44px;top:76px;font-size:16.5px;color:var(--ink);font-weight:400}
  .column{position:absolute;top:102px;width:228px;font-size:7.9px;line-height:12.1px;color:var(--ink);
    text-align:justify;hyphens:auto}
  .column--left{left:44px}
  .column--right{left:285px}
  .column p{margin-bottom:12.1px}

  .contact{position:absolute;left:441px;top:348px;color:var(--white);font-size:5.6px;line-height:9px;list-style:none}
  .contact li{display:flex;align-items:center;gap:4px}
  .contact svg{width:6px;height:6px}
  .contact .addr{margin-top:1px}
</style>
</head>
<body>
<main class="deck">

  <section class="slide slide--title">
    <svg class="art" viewBox="0 0 541 409" preserveAspectRatio="none" aria-hidden="true">
      <path d="M0 0 L22 0 C0 170 190 335 425 409 L0 409 Z" fill="var(--blue)"/>
      <path d="M22 0 L62 0 C24 150 200 320 428 409 L420 409 C190 335 6 170 22 0 Z" fill="var(--black)"/>
      <path d="M22 0 C6 170 190 335 420 409" fill="none" stroke="var(--white)" stroke-width="2"/>
    </svg>
    <div class="brand brand--lg">Ridgeline Components</div>
    <div class="cover-title">
      <h1>CLICK TO ADD TITLE</h1>
      <p>Lorem ipsum dolor sit amet, consec-<br>tetur adipisicing elit, sed do eius-</p>
    </div>
  </section>

  <section class="slide slide--contents">
    <svg class="art" viewBox="0 0 546 409" preserveAspectRatio="none" aria-hidden="true">
      <path d="M0 19 L438 19 C400 26 400 56 438 62 L0 62 Z" fill="var(--blue)"/>
      <path d="M0 336 C40 370 100 395 142 409 L0 409 Z" fill="var(--blue)"/>
      <path d="M0 332 C40 366 110 394 148 409 L142 409 C100 395 40 370 0 338 Z" fill="var(--black)"/>
    </svg>
    <div class="band-title">CLICK TO ADD TITLE</div>
    <div class="brand brand--sm">Ridgeline Components</div>
    <ol class="toc">
      <li>Lorem Ipsum is simply dummy text<span class="lead"></span><span class="num">1</span></li>
      <li class="sub">a) Of the printing and typesetting industry. Lorem Ipsum has been the try's<span class="lead"></span><span class="num">2</span></li>
      <li class="sub">b) Standard dummy text ever since the 1500s, when an unknown printer<span class="lead"></span><span class="num">2</span></li>
      <li>Lorem Ipsum is simply dummy text is the basic dummy text<span class="lead"></span><span class="num">3</span></li>
      <li class="sub">make a type specimen book. It has survived not only five centuries<span class="lead"></span><span class="num">4</span></li>
      <li class="sub">leap into electronic typesetting, remaining<span class="lead"></span><span class="num">5</span></li>
      <li class="sub">larised in the 1960s with the release of transfer sheets containing<span class="lead"></span><span class="num">6</span></li>
      <li>Lorem Ipsum is simply dummy text<span class="lead"></span><span class="num">7</span></li>
      <li>Lorem Ipsum is simply dummy textlorem ipsum is<span class="lead"></span><span class="num">7</span></li>
    </ol>
  </section>

  <section class="slide slide--content">
    <svg class="art" viewBox="0 0 546 409" preserveAspectRatio="none" aria-hidden="true">
      <path d="M0 19 L437 19 C400 26 400 56 437 62 L0 62 Z" fill="var(--blue)"/>
      <path d="M0 340 C40 372 100 396 142 409 L0 409 Z" fill="var(--blue)"/>
      <path d="M0 334 C40 368 110 395 150 409 L142 409 C100 396 40 372 0 340 Z" fill="var(--black)"/>
    </svg>
    <div class="band-title">CLICK TO ADD TITLE</div>
    <div class="brand brand--sm">Ridgeline Components</div>
    <h2 class="body-head">Lorem ipsum dolor sit amet, consectetur adipisicing elit,</h2>
    <div class="column column--left">
      <p>Lorem Ipsum is simply dummy text of the printing and typesetting industry. Lorem Ipsum has been the industry's standard dummy text ever since the 1500s, when an unknown printer took a galley of type and scrambled it to make a type specimen book. It has survived not only five centuries, but also the leap into electronic typesetting, remaining essentially unchanged. It was popularised in the 1960s with the release of transfer sheets containing Lorem Ipsum passages, and more recently with desktop publishing software and common layout tools including versions of Lorem Ipsum.</p>
      <p>It is a long established fact that a reader will be distracted by the readable content of a page when looking at its layout. The point of using Lorem Ipsum is that it has a more-or-less normal distribution of letters, as opposed to using 'Content here, content here', making it look like readable English. Many desktop publishing packages and web page editors now use Lorem Ipsum as their default model text, and a search for 'lorem ipsum' will uncover</p>
    </div>
    <div class="column column--right">
      <p>many web sites still in their infancy. Vari</p>
      <p>Contrary to popular belief, Lorem Ipsum is not simply random text. It has roots in a piece of classical Latin literature from 45 BC, making it over 2000 years old. One scholar, a Latin professor at a small college out east, looked up one of the more obscure Latin words, consectetur, from a Lorem Ipsum passage, and going through the cites of the word in classical literature, discovered the undoubtable source. Lorem Ipsum comes from sections 1.10.32 and 1.10.33 of "de Finibus Bonorum et Malorum" (The Extremes of Good and Evil) by an old author, written in 45 BC. This book is a treatise on the theory of ethics, very popular during the Renaissance. The first line of Lorem Ipsum, "Lorem ipsum dolor sit amet..", comes from a line in section 1.10.32.</p>
      <p>The standard chunk of Lorem Ipsum used since the 1500s is reproduced below for those interested. Sections 1.10.32 and 1.10.33 from "de Finibus Bonorum et Malorum" by</p>
    </div>
  </section>

  <section class="slide slide--closing">
    <svg class="art" viewBox="0 0 546 409" preserveAspectRatio="none" aria-hidden="true">
      <path d="M546 0 L522 0 C560 190 380 340 120 409 L546 409 Z" fill="var(--blue)"/>
      <path d="M522 0 L482 0 C520 160 360 320 112 409 L120 409 C380 340 560 190 522 0 Z" fill="var(--black)"/>
      <path d="M522 0 C560 190 380 340 120 409" fill="none" stroke="var(--white)" stroke-width="2"/>
    </svg>
    <div class="brand brand--foot">Ridgeline Components</div>
    <ul class="contact">
      <li><svg viewBox="0 0 10 10"><circle cx="5" cy="5" r="5" fill="var(--white)"/><path d="M3 2.5l1 1-.6.8a4 4 0 0 0 2.3 2.3l.8-.6 1 1-.7.9C4.5 7.8 2.2 5.5 2.1 3.2z" fill="var(--blue)"/></svg>555.010.4400 ext. 204</li>
      <li><svg viewBox="0 0 10 10"><circle cx="5" cy="5" r="5" fill="var(--white)"/><rect x="2.5" y="3.3" width="5" height="3.4" fill="none" stroke="var(--blue)" stroke-width=".8"/><path d="M2.5 3.3l2.5 2 2.5-2" fill="none" stroke="var(--blue)" stroke-width=".8"/></svg>jdoe@ridgeline.example</li>
      <li><svg viewBox="0 0 10 10"><circle cx="5" cy="5" r="5" fill="var(--white)"/><circle cx="5" cy="5" r="2.6" fill="none" stroke="var(--blue)" stroke-width=".8"/><path d="M2.4 5h5.2" stroke="var(--blue)" stroke-width=".7"/></svg>www.ridgeline.example</li>
      <li class="addr">410 Maple Ave.<br>Springfield, PA 17000</li>
    </ul>
  </section>

</main>
</body>
</html>
```